spot uv business card design for KLT Mechanics

I need a great new business card design best suited for spot uv printing. Details to include are Oliver Haskett 0491227304 wwwkltmech.com.au, oli@kltmech.com.au. Company logo attached.
The design has to be spot uv/varnish optimised!!

```html
<!DOCTYPE html>
<html lang="en">
<head>
<meta charset="utf-8">
<title>KLT Mechanics – Business Card</title>
<link href="https://fonts.googleapis.com/css2?family=Roboto:wght@300;700&display=swap" rel="stylesheet">
<style>
  :root{
    --page:#ffffff;
    --bar:#000000;
    --card:#c4c4c4;
    --texture-light:#cdcdcd;
    --texture-dark:#b9b9b9;
    --brand:#2f5677;
    --dial-card-a:#5d7d98;
    --dial-card-b:#a9b6c2;
    --dial-mono-a:#6a6a6a;
    --dial-mono-b:#d6d6d6;
    --mono:#000000;
  }
  html,body{margin:0;padding:0;overflow:hidden;}
  body{width:1200px;height:1000px;position:relative;background:var(--page);font-family:"Roboto",Arial,sans-serif;}
  .bar{position:absolute;left:0;width:1200px;background:var(--bar);}
  .bar--top{top:0;height:68px;}
  .bar--bottom{top:965px;height:35px;}

  .card{position:absolute;left:58px;width:673px;height:415px;background:var(--card);}
  .card--front{top:94px;}
  .card--back{top:522px;}
  .card__texture{position:absolute;inset:0;
    background:linear-gradient(135deg,var(--texture-light) 0%,var(--texture-dark) 100%);}
  .card svg{position:absolute;left:0;top:0;}

  .contacts{position:absolute;right:39px;top:288px;text-align:right;color:var(--brand);
    font-weight:300;font-size:22px;line-height:31px;margin:0;list-style:none;padding:0;}

  .mono{position:absolute;}
  .mono--front{left:755px;top:197px;}
  .mono--back{left:812px;top:612px;}

  .tone-card{--ink:var(--brand);--dial-fill:url(#dial-card);}
  .tone-mono{--ink:var(--mono);--dial-fill:url(#dial-mono);}

  .dial{fill:var(--dial-fill);}
  .stop-card-a{stop-color:var(--dial-card-a);}
  .stop-card-b{stop-color:var(--dial-card-b);}
  .stop-mono-a{stop-color:var(--dial-mono-a);}
  .stop-mono-b{stop-color:var(--dial-mono-b);}
  .brand-word{fill:var(--ink);font-family:"Roboto",Arial,sans-serif;font-weight:300;}
  .brand-initials{fill:var(--ink);font-family:"Roboto",Arial,sans-serif;font-weight:700;text-anchor:middle;}
  .name{fill:var(--ink);font-family:"Roboto",Arial,sans-serif;font-weight:700;}
  .rule{stroke:var(--ink);stroke-width:4;}
</style>
</head>
<body>
  <div class="bar bar--top"></div>

  <svg width="0" height="0" style="position:absolute" aria-hidden="true">
    <defs>
      <linearGradient id="dial-card" x1="1" y1="0" x2="0" y2="1">
        <stop offset="0" class="stop-card-a"/>
        <stop offset="1" class="stop-card-b"/>
      </linearGradient>
      <linearGradient id="dial-mono" x1="1" y1="0" x2="0" y2="1">
        <stop offset="0" class="stop-mono-a"/>
        <stop offset="1" class="stop-mono-b"/>
      </linearGradient>

      <symbol id="face-front" viewBox="0 0 673 415">
        <path class="dial" transform="translate(200 211)" d="M-131 92 A160 160 0 1 1 131 92 Z"
              role="img" aria-label="Speedometer dial with tick marks, numbers 0 to 10 and a redline band"/>
        <text class="brand-initials" x="197" y="236" font-size="74" letter-spacing="3">KLT</text>
        <text class="brand-word" x="372" y="141" font-size="26">KLT MECHANICS</text>
        <line class="rule" x1="342" y1="206" x2="634" y2="206"/>
        <text class="name" x="372" y="245" font-size="28">Oliver Haskett</text>
      </symbol>

      <symbol id="face-back" viewBox="0 0 673 415">
        <path class="dial" transform="translate(340 243)" d="M-174 122 A212 212 0 1 1 174 122 Z"
              role="img" aria-label="Large speedometer dial with tick marks, numbers 0 to 10 and a redline band"/>
        <text class="brand-word" x="340" y="225" font-size="42" text-anchor="middle">KLT MECHANICS</text>
      </symbol>
    </defs>
  </svg>

  <section class="card card--front tone-card">
    <div class="card__texture" role="img" aria-label="Fine hexagon texture in light grey, spot UV layer"></div>
    <svg width="673" height="415" viewBox="0 0 673 415"><use href="#face-front" width="673" height="415"/></svg>
    <ul class="contacts">
      <li>Phone: 0491227304</li>
      <li>oli@kltmech.com.au</li>
      <li>www.kltmech.com.au</li>
    </ul>
  </section>

  <section class="card card--back tone-card">
    <div class="card__texture" role="img" aria-label="Fine hexagon texture in light grey, spot UV layer"></div>
    <svg width="673" height="415" viewBox="0 0 673 415"><use href="#face-back" width="673" height="415"/></svg>
  </section>

  <svg class="mono mono--front tone-mono" width="400" height="178" viewBox="37 51 597 266" aria-label="Front layout, one-colour spot UV plate">
    <use href="#face-front" width="673" height="415"/>
  </svg>

  <svg class="mono mono--back tone-mono" width="288" height="233" viewBox="122 30 435 353" aria-label="Back layout, one-colour spot UV plate">
    <use href="#face-back" width="673" height="415"/>
  </svg>

  <div class="bar bar--bottom"></div>
</body>
</html>
```